Flaschenetiketten-Design in rechteckiger Grundform für Biermanufaktur
Der Kontakt war sehr professionell und angenehm. Wir wurden hilfreich beraten. Auf unser Feedback haben wir in kurzer Zeit jeweils neue Entwürfe erhalten. Die Zusammenarbeit und der Service war deutlich über unseren Vorstellungen. Wir können KorvaneDeck nur weiterempfehlen!
Zielgruppe
Wir repräsentieren eine Bier-Manufaktur in der Gründungsphase und sind auf der Suche nach einem Designvorschlag für die Flaschenetiketten.
Unsere Zielgruppe sind Liebhaber, die auf der Suche nach dem Speziellen und Lokalen sind. Der Biergenuss abseits des Massenmarktes soll im Entwurf sichtbar/transportiert werden. Die Bier-Manufaktur steht zeitgleich für Trend-Kreationen mit bodenständigem Ursprung.
Aufgabenstellung
Die Herkunft der Gründer Familie aus dem Schweizer Kanton Simplon soll im Vordergrund stehen, hierzu bitte das Familienwappen / einzelne Elemente siehe Dateiupload berücksichtigen.
Das Etikett soll eine rechteckige Grundform haben.
Folgende Angaben sollen sich im Etikett wiederfinden:
- Biersorte: 'Lager' (zukünftig soll es möglich sein, Biersorte auf dem Etikett zu wechseln)
Brand: 'Mostly Grafun'
'Biermanufaktur Walliser Ursprungs'
Die Schrift soll klar und nicht zu verspielt sein.

```html
<!DOCTYPE html>
<html lang="de">
<head>
<meta charset="utf-8">
<title>Mostly Grafun – Lagerbier Etikett</title>
<link rel="stylesheet" href="https://fonts.googleapis.com/css2?family=Josefin+Sans:wght@600;700&display=swap">
<style>
  :root {
    --page: #ffffff;
    --label-ground: #262626;
    --ink-light: #ffffff;
    --gold-light: #fbf6c4;
    --gold-mid: #e6c24a;
    --gold-deep: #a8700f;
    --gold-dark: #7a4a08;
  }
  * { box-sizing: border-box; margin: 0; padding: 0; }
  html, body {
    width: 844px;
    height: 1200px;
    overflow: hidden;
    background: var(--page);
  }
  .canvas {
    position: relative;
    width: 844px;
    height: 1200px;
    display: flex;
    align-items: center;
    justify-content: center;
  }
  .label {
    position: relative;
    width: 620px;
    height: 688px;
    padding: 10px;
    background: linear-gradient(180deg, var(--gold-mid) 0%, var(--gold-light) 18%, var(--gold-deep) 45%, var(--gold-light) 70%, var(--gold-mid) 100%);
    box-shadow: 8px 14px 22px rgba(0, 0, 0, 0.35);
  }
  .label-field {
    width: 100%;
    height: 100%;
    background: var(--label-ground);
    display: flex;
    flex-direction: column;
    align-items: center;
    font-family: "Josefin Sans", sans-serif;
    color: var(--ink-light);
  }
  .crest {
    margin-top: 46px;
    width: 230px;
    height: 278px;
    background: linear-gradient(180deg, var(--gold-light) 0%, var(--gold-light) 25%, var(--gold-mid) 50%, var(--gold-dark) 75%, var(--gold-light) 100%);
    border-radius: 4px 4px 50% 50% / 4px 4px 18% 18%;
  }
  .beer-type {
    margin-top: 30px;
    font-size: 27px;
    font-weight: 600;
    letter-spacing: 0.12em;
  }
  .brand-name {
    margin-top: 44px;
    font-size: 92px;
    font-weight: 700;
    line-height: 0.94;
    letter-spacing: 0.05em;
    text-align: center;
  }
  .tagline {
    margin-top: 22px;
    font-size: 19px;
    font-weight: 600;
    letter-spacing: 0.14em;
  }
</style>
</head>
<body>
  <main class="canvas">
    <section class="label">
      <div class="label-field">
        <div class="crest" role="img" aria-label="Goldenes Familienwappen mit Sternen, Kreuz und Reichsapfel"></div>
        <p class="beer-type">- LAGERBIER -</p>
        <h1 class="brand-name">MOSTLY<br>GRAFUN</h1>
        <p class="tagline">BIERMANUFAKTUR WALLISER URSPRUNGS</p>
      </div>
    </section>
  </main>
</body>
</html>
```